Coral Journey Mate - A Travel Services Website

Sunreef Home Rentals is a company that provides travels services to home owners and travellers to Barbados. Coral Journey Mate is a particular brand targeting travelling guests with specific set of travel services. The brand slogan is:

'Getting you the best for less'

The travel services will include:

- Coral Journey Mate Perks Pass
- Car Hire Quote Service
- Mobile Phone Sim Cards
- Prepaid Debit Cards
- Airport Hotel Booking
- Airport Lounge Booking
- Airport Parking

There will also be a travel planner function for guests.

The main puropse of the site is as follows:

1. Registration for the Coral Journey Mate Perks Pass

2. Creation of user account which the guest will frequently return to check for updates

3. Purchase of ancillary travel products and services

4. To use the Travel Planner

5. To gather data on holiday home owners in Barbados

A site map can be seen at the following link:

http://plotgridly.example/outlines/viewMap/4kqzvbn8ytrwpa2fuh5ximc07jldg6sqenoa9rvb33kf2pyq71

Webpage templates (2 required)

The first will be form control heavy (text boxes, checkboxes ect). It will need failure and success messages / indicators etc.

The second will be a general content area with a secondary navigation area (i.e for sub sections of the current section). This will house text / headings and images.

Both will require header, primary navigation, content and footer areas.

N.B. Please not that I am not technical and the above webtemplate narrative has been supplied by my web developer/programmer. If you have any questions, please ask me any questions and I will get an answer from him.

Target Market(s)

My customers tend to be:

Sex: Female
Age: 24-55
Location: UK, USA, Canada
Social Class: A,B,C1
Income: Medium income bracket

They are possibly visiting Barbados for the first and only time. It is an expensive destination and is accessible to people with a medium to high income. They still desire 'value for money'. Therefore the sight must give guests confidence that Coral Journey Mate is 'their friend', is seeking to offer the best value deals for their vacation/holiday.

Industry/Entity Type

Travel

Requirements
Must have
• The site templates must be professional, aspirational, trustworthy, reassuring, clean, innovative, fun. When people visit the site they should be excited about the savings that they can make and want to return as there is a perceived benefit for them. It must look expensive and professional in its projected image.
Nice to have
• Smooth currved lines, seperated boxed areas for content, as simple and uncluttered layout and it must be simple to read!
Should not have
• It should not be cartoonly, despite my attached logo and must not look cheap.

```html
<!DOCTYPE html>
<html lang="en">
<head>
<meta charset="utf-8">
<title>Coral Journey Mate – Car Hire Dashboard</title>
<link rel="stylesheet" href="https://fonts.googleapis.com/css2?family=Arimo:wght@400;700&family=Baloo+2:wght@700;800&display=swap">
<style>
:root{
  --sky:#d6f1fc;
  --sky-edge:#5cc6ea;
  --blue:#27b3e4;
  --blue-dark:#0d8fc2;
  --orange:#f39a22;
  --orange-dark:#d8660e;
  --orange-light:#fbb944;
  --ink:#222;
  --ink-soft:#444;
  --pill:#2c2c2c;
  --row:#eeeeee;
  --panel:#f0f0f0;
  --white:#fff;
  --brand-red:#d9262c;
  --hero-top:#4f9ad6;
  --hero-bottom:#42b4cf;
}
*{box-sizing:border-box;margin:0;padding:0}
html,body{width:947px;height:1200px;overflow:hidden}
body{position:relative;font-family:"Arimo",Arial,sans-serif;color:var(--ink);
  background:linear-gradient(to bottom,var(--sky) 0,#eef9fe 460px,var(--white) 520px)}
.abs{position:absolute}

/* login */
.login-field{position:absolute;top:20px;height:21px;border:1px solid #bfe3f1;border-radius:11px;background:var(--white);
  font-size:9px;color:var(--ink-soft);padding:5px 0 0 10px}
.forgot{left:735px;top:46px;font-size:8px;color:#333;text-decoration:underline}
.login-btn{left:850px;top:47px;width:48px;height:16px;border-radius:8px;font-size:9px;font-weight:700;color:var(--white);
  background:linear-gradient(var(--sky-edge),var(--blue-dark));text-align:center;line-height:16px}

/* primary nav */
.main-nav{left:48px;top:79px;width:850px;height:26px;border-radius:8px;
  background:linear-gradient(#f8a53a,#ec7d12 55%,#d85f0c);display:flex;align-items:center;justify-content:space-between;padding:0 20px;
  box-shadow:0 1px 0 #b54f08}
.main-nav span{color:var(--white);font-weight:700;font-size:12px}
.main-nav i{width:1px;height:14px;background:rgba(255,255,255,.8)}

/* hero */
.hero{left:48px;top:123px;width:850px;height:328px;border:2px solid var(--sky-edge);border-radius:10px;overflow:hidden}
.hero-photo{position:absolute;inset:0;background:linear-gradient(to bottom,var(--hero-top),var(--hero-bottom))}
.brand{position:absolute;left:22px;top:30px;display:flex;align-items:center;gap:10px}
.brand-dot{width:50px;height:50px;border-radius:50%;background:var(--orange)}
.brand-name{font-weight:700;font-size:34px;color:var(--brand-red);line-height:1}
.slogan{position:absolute;left:18px;top:118px;font-family:"Baloo 2",sans-serif;font-weight:800;font-size:24px;color:#f6c51a}
.hero-cta{position:absolute;left:27px;top:188px;width:300px;height:79px;border-radius:9px;
  background:linear-gradient(#fcc04e,#f39a22 55%,#e27f14);display:flex;align-items:center;padding-left:22px;
  font-family:"Baloo 2",sans-serif;font-weight:800;font-size:27px;color:#1c1c1c;gap:10px}

/* pills */
.pill{position:absolute;top:471px;height:21px;border-radius:11px;background:var(--pill);color:var(--white);
  font-size:12px;font-weight:700;line-height:21px;padding-left:12px}
.request-btn{left:775px;top:471px;width:123px;height:23px;border-radius:12px;text-align:center;line-height:23px;
  font-size:12px;font-weight:700;color:var(--white);background:linear-gradient(#7fd7f5,var(--blue) 60%,var(--blue-dark));
  border:1px solid var(--blue-dark)}

/* sidebar */
.welcome{left:66px;top:505px;font-size:10px;font-weight:700}
.side-nav{left:48px;top:531px;width:220px;background:var(--panel);list-style:none;padding:1px 0}
.side-nav li{height:27px;border-bottom:1px solid #fafafa;font-size:10px;line-height:27px;padding-left:12px;display:flex;gap:10px}
.side-nav li:last-child{border-bottom:0}
.side-nav b{font-size:11px}
.promo{width:221px;border-radius:10px;overflow:hidden;border:2px solid}
.promo-art{position:absolute;inset:0}
.promo-title{position:relative;font-family:"Baloo 2",sans-serif;font-weight:800;font-size:27px;color:var(--white);
  text-align:center;line-height:32px;-webkit-text-stroke:1.5px #333;paint-order:stroke fill}
.promo-trip{left:47px;top:684px;height:146px;border-color:#e8901c}
.promo-trip .promo-art{background:radial-gradient(circle at 60% 60%,#fde2a4,#f6a83a 55%,#e47e16)}
.promo-trip .promo-title{margin-top:38px}
.promo-places{left:48px;top:846px;height:141px;border-color:#2ba9d6}
.promo-places .promo-art{background:linear-gradient(#7fd4f2,#2fb6e6 55%,#1a8cc4)}
.promo-places .promo-title{margin-top:36px}

/* tables */
.section-title{left:295px;font-size:13px;font-weight:700;color:var(--orange)}
.section-title small{font-size:10px;color:var(--ink);font-weight:400;margin-left:6px}
.grid{position:absolute;left:295px;width:600px}
.grid .row{display:flex;align-items:center;height:19.2px}
.cols{display:flex;width:511px;height:15px;align-items:center}
.row.data .cols{background:var(--row)}
.cols span{text-align:center;font-size:8.5px;white-space:nowrap}
.head .cols span{color:var(--blue);font-weight:700;font-size:9.5px}
.cols span:nth-child(1){width:82px}.cols span:nth-child(2){width:83px}.cols span:nth-child(3){width:83px}
.cols span:nth-child(4){width:74px}.cols span:nth-child(5){width:68px}.cols span:nth-child(6){width:66px}
.cols span:nth-child(7){width:55px}
.btn{height:15px;width:31px;border-radius:3px;font-size:8px;text-align:center;line-height:15px;color:var(--white)}
.btn-view{margin-left:12px;background:linear-gradient(#8fdcf7,var(--blue))}
.btn-cancel{margin-left:5px;background:#111}

/* footer */
.footer{left:0;top:1099px;width:947px;height:101px;background:linear-gradient(#f9b347,#f39a22 50%,#ee8a17)}
.footer-div{position:absolute;top:0;width:1px;height:101px;background:#d9720e;box-shadow:1px 0 0 #fbc46a}
.copyright{position:absolute;left:0;width:293px;top:41px;text-align:center;font-size:8.5px;font-weight:700;color:var(--white);line-height:11px}
.call{position:absolute;left:293px;width:239px;top:26px;text-align:center;color:var(--white);font-weight:700}
.call-label{font-size:17px}
.call-number{font-size:27px;margin-top:4px}
.testimonials{position:absolute;left:576px;top:14px;width:320px;color:var(--white)}
.testimonials h3{font-size:12px}
.testimonials p{font-size:9px;font-style:italic;font-weight:700;line-height:11.5px;margin-top:7px;padding-left:15px}
.quote-mark{position:absolute;font-size:26px;color:#fbd08a;font-family:Georgia,serif;font-weight:700}
</style>
</head>
<body>

<div class="login-field" style="left:547px;width:169px">User name</div>
<div class="login-field" style="left:727px;width:171px">Password</div>
<div class="abs forgot">Forgot Password?</div>
<div class="abs login-btn">Log in</div>

<nav class="abs main-nav">
  <span>Home</span><i></i><span>Airport Parking</span><i></i><span>Airport Hotel</span><i></i><span>Car Hire</span><i></i>
  <span>Attractions</span><i></i><span>Travel Money</span><i></i><span>Mobile Simcards</span><i></i><span>Privilege Card</span>
</nav>

<header class="abs hero">
  <div class="hero-photo" role="img" aria-label="Photo of a tropical beach with a traveller waving from a hire car"></div>
  <div class="brand"><div class="brand-dot"></div><div class="brand-name">Coral Journey Mate</div></div>
  <div class="slogan">'Getting you the best for less'</div>
  <div class="hero-cta">Hire Your Car Now
    <svg width="34" height="22" viewBox="0 0 34 22"><path d="M2 2l9 9-9 9M15 2l9 9-9 9" fill="none" stroke="#1c1c1c" stroke-width="5"/></svg>
  </div>
</header>

<div class="pill" style="left:48px;width:147px">Account Dashboard:</div>
<div class="pill" style="left:288px;width:124px">Car Hire:</div>
<div class="abs request-btn">Request Prices</div>

<div class="abs welcome">Welcome ! Marcus L. D.</div>
<ul class="abs side-nav">
  <li><b>›</b>Home</li>
  <li><b>›</b>Preparation List</li>
  <li><b>›</b>Get a Coral Perks Pass</li>
  <li><b>›</b>Get Car Here</li>
  <li><b>›</b>Settings</li>
</ul>

<div class="abs promo promo-trip">
  <div class="promo-art" role="img" aria-label="Passenger plane flying into a warm orange sky"></div>
  <div class="promo-title">Book Your<br>Trip Now</div>
</div>
<div class="abs promo promo-places">
  <div class="promo-art" role="img" aria-label="Turquoise Caribbean water and palm tree"></div>
  <div class="promo-title">Barbados<br>Locations</div>
</div>

<div class="abs section-title" style="top:528px">Open Quotes:</div>
<div class="grid" style="top:549px">
  <div class="row head"><div class="cols"><span>Pick Up Location</span><span>Date</span><span>Drop Off Location</span><span>Date</span><span>Driver's Age</span><span>Car Group</span><span>Currency</span></div></div>
  <div class="row data"><div class="cols"><span>Florida Airport</span><span>15-09-2010</span><span>Beach Side</span><span>18-09-2010</span><span>32 Years</span><span>Family</span><span>$</span></div><div class="btn btn-view">View</div><div class="btn btn-cancel">Cancel</div></div>
  <div class="row data"><div class="cols"><span>Florida Airport</span><span>15-09-2010</span><span>Beach Side</span><span>18-09-2010</span><span>32 Years</span><span>Family</span><span>$</span></div><div class="btn btn-view">View</div><div class="btn btn-cancel">Cancel</div></div>
  <div class="row data"><div class="cols"><span>Florida Airport</span><span>15-09-2010</span><span>Beach Side</span><span>18-09-2010</span><span>32 Years</span><span>Family</span><span>$</span></div><div class="btn btn-view">View</div><div class="btn btn-cancel">Cancel</div></div>
</div>

<div class="abs section-title" style="top:654px">Accepted Quotes:<small>(The Hire Provider Still Needs to confirm booking)</small></div>
<div class="grid" style="top:676px">
  <div class="row head"><div class="cols"><span>Pick Up Location</span><span>Date</span><span>Drop Off Location</span><span>Date</span><span>Driver's Age</span><span>Car Group</span><span>Currency</span></div></div>
  <div class="row data"><div class="cols"><span>Florida Airport</span><span>15-09-2010</span><span>Beach Side</span><span>18-09-2010</span><span>32 Years</span><span>Family</span><span>$</span></div><div class="btn btn-view">View</div><div class="btn btn-cancel">Cancel</div></div>
  <div class="row data"><div class="cols"><span>Florida Airport</span><span>15-09-2010</span><span>Beach Side</span><span>18-09-2010</span><span>32 Years</span><span>Family</span><span>$</span></div><div class="btn btn-view">View</div><div class="btn btn-cancel">Cancel</div></div>
  <div class="row data"><div class="cols"><span>Florida Airport</span><span>15-09-2010</span><span>Beach Side</span><span>18-09-2010</span><span>32 Years</span><span>Family</span><span>$</span></div><div class="btn btn-view">View</div><div class="btn btn-cancel">Cancel</div></div>
</div>

<div class="abs section-title" style="top:777px">Confirmed Bookings:</div>
<div class="grid" style="top:798px">
  <div class="row head"><div class="cols"><span>Pick Up Location</span><span>Date</span><span>Drop Off Location</span><span>Date</span><span>Driver's Age</span><span>Car Group</span><span>Currency</span></div></div>
  <div class="row data"><div class="cols"><span>Florida Airport</span><span>15-09-2010</span><span>Beach Side</span><span>18-09-2010</span><span>32 Years</span><span>Family</span><span>$</span></div><div class="btn btn-view">View</div></div>
  <div class="row data"><div class="cols"><span>Florida Airport</span><span>15-09-2010</span><span>Beach Side</span><span>18-09-2010</span><span>32 Years</span><span>Family</span><span>$</span></div><div class="btn btn-view">View</div></div>
  <div class="row data"><div class="cols"><span>Florida Airport</span><span>15-09-2010</span><span>Beach Side</span><span>18-09-2010</span><span>32 Years</span><span>Family</span><span>$</span></div><div class="btn btn-view">View</div></div>
  <div class="row data"><div class="cols"><span>Florida Airport</span><span>15-09-2010</span><span>Beach Side</span><span>18-09-2010</span><span>32 Years</span><span>Family</span><span>$</span></div><div class="btn btn-view">View</div></div>
  <div class="row data"><div class="cols"><span>Florida Airport</span><span>15-09-2010</span><span>Beach Side</span><span>18-09-2010</span><span>32 Years</span><span>Family</span><span>$</span></div><div class="btn btn-view">View</div></div>
  <div class="row data"><div class="cols"><span>Florida Airport</span><span>15-09-2010</span><span>Beach Side</span><span>18-09-2010</span><span>32 Years</span><span>Family</span><span>$</span></div><div class="btn btn-view">View</div></div>
  <div class="row data"><div class="cols"><span>Florida Airport</span><span>15-09-2010</span><span>Beach Side</span><span>18-09-2010</span><span>32 Years</span><span>Family</span><span>$</span></div><div class="btn btn-view">View</div></div>
  <div class="row data"><div class="cols"><span>Florida Airport</span><span>15-09-2010</span><span>Beach Side</span><span>18-09-2010</span><span>32 Years</span><span>Family</span><span>$</span></div><div class="btn btn-view">View</div></div>
  <div class="row data"><div class="cols"><span>Florida Airport</span><span>15-09-2010</span><span>Beach Side</span><span>18-09-2010</span><span>32 Years</span><span>Family</span><span>$</span></div><div class="btn btn-view">View</div></div>
  <div class="row data"><div class="cols"><span>Florida Airport</span><span>15-09-2010</span><span>Beach Side</span><span>18-09-2010</span><span>32 Years</span><span>Family</span><span>$</span></div><div class="btn btn-view">View</div></div>
  <div class="row data"><div class="cols"><span>Florida Airport</span><span>15-09-2010</span><span>Beach Side</span><span>18-09-2010</span><span>32 Years</span><span>Family</span><span>$</span></div><div class="btn btn-view">View</div></div>
  <div class="row data"><div class="cols"><span>Florida Airport</span><span>15-09-2010</span><span>Beach Side</span><span>18-09-2010</span><span>32 Years</span><span>Family</span><span>$</span></div><div class="btn btn-view">View</div></div>
</div>

<footer class="abs footer">
  <div class="footer-div" style="left:293px"></div>
  <div class="footer-div" style="left:532px"></div>
  <div class="copyright">Copyright © 2010 Coral Journey Mate<br>All Rights Reserved.</div>
  <div class="call"><div class="call-label">Call Now</div><div class="call-number">111 555 208</div></div>
  <div class="quote-mark" style="left:572px;top:32px">“</div>
  <div class="testimonials">
    <h3>Testimonials:</h3>
    <p>Lorem Ipsum is simply dummy text of the printing and typesetting industry. Lorem Ipsum has been the industry's standard dummy text ever since the 1500s, when an unknown printer took a galley of type and scrambled it to make a type specimen book.</p>
  </div>
  <div class="quote-mark" style="left:880px;top:76px">”</div>
</footer>

</body>
</html>
```